Portfolio site - Need a basic WordPress or SquareSpace site

I need a portfolio site where I have the option to keep updating it on my own. Therefore, I'm guessing I need one that uses WordPress or SquareSpace. I just need a simple and elegant design. I'm a writer (scholarly, fiction and journalism).

Target Market(s)

Adult

Industry/Entity Type

Writer

Number of Pages Required

4 page

Font styles to use
Serif

Colors
b7a5cd
e667a6
85abd2

Requirements
Must have
• Easily updatable features. I'll have to publish links and small blurbs from time to time. And maybe the occasional image.
• Pages should be:
• Home
• Work
• Press
• Contact

```html
<!DOCTYPE html>
<html lang="en">
<head>
<meta charset="utf-8">
<title>Noor Almasi — Writer and Comics Scholar</title>
<link href="https://fonts.googleapis.com/css2?family=Caveat+Brush&family=Encode+Sans+Condensed:wght@300;400&family=Special+Elite&display=swap" rel="stylesheet">
<style>
  :root{
    --pink:#e667a6;
    --lavender:#b7a5cd;
    --black:#000;
    --plum:#7c0f52;
    --plum-dark:#4e0b33;
    --grey:#8a8a8a;
    --ink:#1a1a1a;
    --footer:#222;
  }
  *{margin:0;padding:0;box-sizing:border-box}
  html,body{width:942px;height:1200px;overflow:hidden}
  body{position:relative;font-family:"Encode Sans Condensed",sans-serif;font-weight:300;background:var(--pink)}
  .site-header{position:absolute;top:0;left:0;width:942px;height:70px;background:var(--pink);border-top:2px solid #333;border-bottom:1px solid #b84e85}
  .brand{position:absolute;left:96px;top:26px;font-family:"Special Elite",cursive;font-size:18px;color:var(--ink)}
  .main-nav{position:absolute;right:95px;top:28px;display:flex;gap:15px;align-items:center}
  .main-nav a{font-family:"Caveat Brush",cursive;font-size:14px;letter-spacing:1.3px;text-transform:uppercase;color:var(--ink);text-decoration:none}
  .main-nav a.current{color:#a8356f}
  .search-icon{width:10px;height:10px}
  .hero{position:absolute;top:70px;left:0;width:942px;height:348px;background:var(--black)}
  .hero-portrait{position:absolute;left:0;top:0;width:472px;height:348px;background:radial-gradient(ellipse 45% 55% at 55% 45%,#b02b6a 0%,#6d1742 45%,#000 85%)}
  .hero-text{position:absolute;left:471px;top:105px;width:370px}
  .hero-title{font-family:"Caveat Brush",cursive;font-style:italic;font-weight:400;font-size:21px;line-height:23px;color:var(--plum);transform:skewX(-8deg)}
  .hero-blurb{margin-top:26px;font-size:12px;line-height:23px;color:#6f6f6f}
  .hero-link{display:inline-block;margin-top:24px;margin-left:8px;font-family:"Caveat Brush",cursive;font-size:13px;color:var(--plum);text-decoration:none}
  .feature{position:absolute;top:418px;left:0;width:942px;height:397px;background:var(--lavender)}
  .feature-text{position:absolute;left:95px;top:110px;width:345px}
  .section-title{font-family:"Caveat Brush",cursive;font-style:italic;font-weight:400;font-size:17px;line-height:20px;color:var(--plum-dark)}
  .feature-blurb{margin-top:34px;font-size:12px;line-height:23px;color:#5c5566}
  .btn{display:inline-block;border:2px solid var(--plum-dark);border-radius:2px;padding:6px 14px;font-family:"Caveat Brush",cursive;font-size:13px;color:var(--plum-dark);text-decoration:none;box-shadow:0 2px 6px rgba(0,0,0,.35)}
  .feature .btn{margin-top:21px}
  .book-cover{position:absolute;left:632px;top:63px;width:171px;height:271px;background:linear-gradient(160deg,#4c8f93 0%,#b3413a 45%,#6e6a56 75%,#44505c 100%);border-left:12px solid #111;box-shadow:2px 3px 6px rgba(0,0,0,.3)}
  .bio{position:absolute;top:815px;left:0;width:942px;height:355px;background:var(--pink)}
  .bio-photo{position:absolute;left:95px;top:57px;width:125px;height:125px;border-radius:50%;border:3px solid var(--black);background:radial-gradient(circle at 50% 45%,#6b4a3c 0%,#3a2b25 55%,#5a4a30 100%)}
  .bio-text{position:absolute;left:293px;top:60px;width:558px}
  .bio-text .section-title{color:var(--plum-dark)}
  .bio-body{margin-top:26px;font-size:12px;line-height:23.3px;color:#5a2440}
  .bio .btn{margin-top:22px}
  .site-footer{position:absolute;top:1170px;left:0;width:942px;height:30px;background:var(--footer);color:#fff;font-family:"Encode Sans Condensed",sans-serif;font-weight:400;font-size:9px}
  .copyright{position:absolute;left:95px;top:10px}
  .social{position:absolute;right:95px;top:10px;font-size:9px}
</style>
</head>
<body>
  <header class="site-header">
    <div class="brand">Noor Almasi</div>
    <nav class="main-nav">
      <a class="current" href="#">Home</a>
      <a href="#">About</a>
      <a href="#">Work</a>
      <a href="#">Press</a>
      <a href="#">Contact</a>
      <svg class="search-icon" viewBox="0 0 10 10" aria-label="Search"><circle cx="6" cy="4" r="3" fill="none" stroke="#1a1a1a" stroke-width="1.2"/><line x1="3.8" y1="6.2" x2="1" y2="9" stroke="#1a1a1a" stroke-width="1.2"/></svg>
    </nav>
  </header>

  <section class="hero">
    <div class="hero-portrait" role="img" aria-label="Pink halftone dot portrait of the writer on black"></div>
    <div class="hero-text">
      <h1 class="hero-title">The Comics Writer Who Wants More Authentic Female Muslim Superheroes</h1>
      <p class="hero-blurb">Comics scholar Noor Almasi explores how superheroes like Sandstorm and Miss Nova can both perpetuate and subvert stereotypes.</p>
      <a class="hero-link" href="#">Read More →</a>
    </div>
  </section>

  <section class="feature">
    <div class="feature-text">
      <h2 class="section-title">1001 Harbourside Nights, Queen Street Tales (Lakeshore Comics Anthology)</h2>
      <p class="feature-blurb">Two women enlist the help of a rookie genie in a desperate bid to keep the Dar Zaytun cultural centre open.</p>
      <a class="btn" href="#">Queen Street Tales on Pageleaf</a>
    </div>
    <div class="book-cover" role="img" aria-label="Cover of the Queen Street Tales comics anthology with a dragon over a city street"></div>
  </section>

  <section class="bio">
    <div class="bio-photo" role="img" aria-label="Round photo of the writer holding the anthology in a bookshop"></div>
    <div class="bio-text">
      <h2 class="section-title">Noor Almasi</h2>
      <p class="bio-body">Noor Almasi is a writer and comics scholar. She recently published her first short story comic, “1001 Harbourside Nights” in the Queen Street Tales Anthology which was illustrated by Lena Varo. As a comics scholar, her research interests are mainly focused on Muslimah and intersectional superheroes, as well as racialized women in comics. She most recently completed an audience analysis of young adult Muslim consumers of comics, and is currently working on more fiction and scholarly projects. She lives in Toronto, Ontario.</p>
      <a class="btn" href="#">Read More</a>
    </div>
  </section>

  <footer class="site-footer">
    <span class="copyright">Copyright © 2018 Noor Almasi</span>
    <span class="social">Chatterline</span>
  </footer>
</body>
</html>
```